Saltbush Creek Plumbing Business card & letter head design

We need a new business card and letter head for our plumbing company called saltbush creek plumbing. attached is the companys logo. We provide domestic and commercial plumbing services in regional western Australia. We are after Something simple yet nice to look at and something that fits within the trade industry.

Target Market(s)

trade/building industry

Contact Information for Business Card

Harlan Mossby
Manager
0481 362 740
enquiries@scplumbingco.net.au
ABN: 47 815 203 966
PCL: 4187

Domestic & Commercial Plumbing
Tip Truck & Excavator hire

Colors

Designer to choose colors to be used in the design.

```html
<!DOCTYPE html>
<html lang="en">
<head>
<meta charset="utf-8">
<title>Saltbush Creek Plumbing — Business Card</title>
<link href="https://fonts.googleapis.com/css2?family=Roboto:wght@400;500;700&display=swap" rel="stylesheet">
<style>
  :root {
    --canvas: #d9d9da;
    --card-white: #ffffff;
    --card-dark: #1b1e23;
    --brand-blue: #1c5fb5;
    --brand-grey: #5a5d62;
    --text-grey: #55585c;
    --rule: #8a8d92;
    --tagline: #f2f3f5;
  }
  * { box-sizing: border-box; margin: 0; padding: 0; }
  html, body {
    width: 1200px; height: 800px; overflow: hidden;
    background: var(--canvas);
    font-family: "Roboto", Arial, sans-serif;
  }
  .stage {
    width: 1200px; height: 800px;
    display: flex; align-items: center; justify-content: center; gap: 40px;
  }
  .card {
    width: 560px; height: 320px; position: relative; overflow: hidden;
    box-shadow: 0 6px 18px rgba(0,0,0,0.18);
  }
  /* Front */
  .card-front {
    background: var(--card-white);
    display: flex; flex-direction: column; align-items: center; justify-content: center;
    text-align: center;
  }
  .brand-name {
    font-weight: 700; font-size: 27px; color: var(--brand-blue);
    text-transform: uppercase; letter-spacing: 0.5px; line-height: 1;
  }
  .brand-rule {
    width: 300px; height: 1px; background: var(--rule); margin: 8px 0 18px;
  }
  .person-name {
    font-weight: 700; font-size: 21px; color: var(--brand-blue);
    text-transform: uppercase; line-height: 1;
  }
  .person-role {
    font-size: 13px; color: var(--text-grey); margin-top: 4px;
  }
  .person-rule {
    width: 150px; height: 1px; background: var(--rule); margin: 6px 0 18px;
  }
  .registration {
    font-size: 13px; color: var(--text-grey); margin-bottom: 14px;
  }
  .contact-line {
    display: flex; align-items: center; gap: 6px;
    font-size: 14px; color: var(--text-grey); margin-bottom: 6px;
  }
  .contact-line svg { width: 13px; height: 13px; fill: var(--brand-blue); }
  /* Back */
  .card-back { background: var(--card-dark); }
  .back-texture {
    position: absolute; inset: 0;
    background: linear-gradient(135deg, #1f2631 0%, #1b1e23 55%, #1d2430 100%);
  }
  .back-brand {
    position: absolute; right: 32px; top: 120px;
    font-weight: 700; font-size: 26px; color: var(--brand-blue);
    text-transform: uppercase; text-align: right; line-height: 1.1;
  }
  .tagline {
    position: absolute; left: 32px; bottom: 30px;
    font-weight: 500; font-size: 15px; color: var(--tagline); line-height: 1.35;
  }
</style>
</head>
<body>
  <main class="stage">
    <section class="card card-front">
      <div class="brand-name">Saltbush Creek Plumbing</div>
      <div class="brand-rule"></div>
      <div class="person-name">Harlan Mossby</div>
      <div class="person-role">Manager</div>
      <div class="person-rule"></div>
      <div class="registration">ABN: 47 815 203 966 &nbsp;PCL: 4187</div>
      <div class="contact-line">
        <svg viewBox="0 0 24 24" aria-hidden="true"><path d="M6.6 10.8a15.1 15.1 0 0 0 6.6 6.6l2.2-2.2a1 1 0 0 1 1-.25 11.4 11.4 0 0 0 3.6.57 1 1 0 0 1 1 1V20a1 1 0 0 1-1 1A17 17 0 0 1 3 4a1 1 0 0 1 1-1h3.5a1 1 0 0 1 1 1c0 1.25.2 2.45.57 3.6a1 1 0 0 1-.25 1z"/></svg>
        <span>0481 362 740</span>
      </div>
      <div class="contact-line">
        <svg viewBox="0 0 24 24" aria-hidden="true"><path d="M2 5h20v14H2z M2 5l10 8 10-8" fill="var(--brand-blue)"/><path d="M3 6l9 7 9-7" fill="none" stroke="#fff" stroke-width="1.6"/></svg>
        <span>enquiries@scplumbingco.net.au</span>
      </div>
    </section>

    <section class="card card-back">
      <div class="back-texture" role="img" aria-label="Faint repeating brand pattern in dark navy tones"></div>
      <div class="back-brand">Saltbush Creek<br>Plumbing</div>
      <div class="tagline">Domestic &amp; Commercial Plumbing<br>Tip Truck &amp; Excavator hire</div>
    </section>
  </main>
</body>
</html>
```